Need Instructors for martial arts school - special flyers to help

We are a kung fu and tai chi martial arts school and we need to appeal to a certain demographic - 16-30, driven, fit, personable - who can join our team of instructors to help grow our school. We envisage this flyer as as roughly between A6 and A7 in size. The kind of thing we can hand to some one we meet and they can easily stick it in a pocket but not so small it gets lost like a business card. We are a professional and serious organisation so don't want to go too dramatic or cheesy to get attention but the design needs to capture the attention of the reader quickly and keep them engaged. Martial arts has quite a bit of material to use for this purpose. NOTE: we are not Karate or Tae Kwon Do - the difference matters. We will upload our current logo and the text we want to use is this for the front:
"Challenge Yourself...
Teaching is the highest form of learning. Be a part of a professional, dedicated team, delivering the highest level Kung Fu...
Copper Heron Martial Arts"
On the back side it should say:
"Seeking martial arts instructors!
We train in one of the world's most effective martial art systems, Choy Li Fut Kung Fu. As an instructor, you will teach both beginner and intermediate level Kung Fu skills to adults and children at Copper Heron Martial Arts, Brisbane's premier martial arts school.
As an instructor, you will:
- Teach fundamentals to children and adults of all ages and abilities
- Progress student's martial arts and life skills
- Deliver fun and engaging classes
- Develop and grow your martial arts skills at an advanced level and pace
In return, you will receive your training tuition, which includes our high level instructor training program, until qualified and then a weekly one one on one with our very own Sifu, as well as one hour training sessions, twice a week , with our team.
At CHMA our motto is "Challenge yourself... for life!"
Contact us on 0417 863 120 to discuss your interest and suitability - ask for Sifu Rory."
There are two fonts we are liking right now for our designs, Merienda One and Red Rose from Google Fonts.
We basically need this to be cool enough to keep someone's attention and not have them throw it away before they have read it.
Info about us on copperheron.com.au

```html
<!DOCTYPE html>
<html lang="en">
<head>
<meta charset="utf-8">
<title>Copper Heron Martial Arts – Instructor Flyer</title>
<link href="https://fonts.googleapis.com/css2?family=Merienda:wght@400;700&family=Red+Rose:wght@400;500;600&display=swap" rel="stylesheet">
<style>
  :root {
    --canvas: #e8e5e1;
    --paper: #ffffff;
    --red: #e31e2d;
    --ink: #2b2627;
    --text: #2f2b2c;
    --sky-top: #b8c5d1;
    --sky-mid: #d9e0e6;
    --floor-light: #cfc7bb;
    --floor-dark: #b3a795;
    --mist: #f5f6ef;
    --grass-light: #a9cd86;
    --grass-dark: #5c9a3c;
    --script: "Merienda", "Merienda One", cursive;
    --sans: "Red Rose", sans-serif;
  }
  * { box-sizing: border-box; margin: 0; padding: 0; }
  html, body {
    width: 1200px; height: 900px; overflow: hidden;
    background: var(--canvas);
  }
  .canvas { position: relative; width: 1200px; height: 900px; }

  .flyer {
    position: absolute;
    width: 540px; height: 381px;
    background: var(--paper);
    overflow: hidden;
    box-shadow: 0 4px 14px rgba(0,0,0,0.15);
  }
  .flyer--front { left: 40px; top: 150px; }
  .flyer--back { left: 620px; top: 380px; }

  /* brand lockup */
  .brand { position: absolute; display: flex; align-items: center; gap: 8px; }
  .brand__name {
    font-family: var(--sans);
    font-size: 15px; line-height: 15px; color: var(--ink); font-weight: 400;
  }
  .brand__tagline {
    font-family: var(--script); font-weight: 400;
    font-size: 8px; color: var(--red); margin-top: 3px; white-space: nowrap;
  }
  .brand__mark {
    width: 57px; height: 57px; border-radius: 50%;
    border: 1.5px solid var(--ink); background: var(--paper);
    flex: none;
  }

  /* front */
  .front__photo {
    position: absolute; left: 0; top: 0; width: 430px; height: 357px;
    background: linear-gradient(to bottom, var(--sky-top) 0%, var(--sky-mid) 62%, var(--floor-light) 72%, var(--floor-dark) 100%);
    -webkit-mask-image: linear-gradient(to right, #000 50%, transparent 100%);
    mask-image: linear-gradient(to right, #000 50%, transparent 100%);
  }
  .front__headline {
    position: absolute; left: 222px; top: 16px;
    font-family: var(--script); color: var(--red);
    font-size: 48px; line-height: 52px; font-weight: 700;
    white-space: nowrap;
  }
  .front__headline span { display: block; }
  .front__headline span + span { padding-left: 48px; }
  .front__body {
    position: absolute; left: 231px; top: 163px; width: 300px;
    font-family: var(--sans); color: var(--text);
    font-size: 14px; line-height: 26px; white-space: nowrap;
  }
  .front__brand { left: 341px; top: 293px; }
  .flyer__band { position: absolute; left: 0; bottom: 0; }

  /* back */
  .back__photo {
    position: absolute; left: 0; top: 55px; width: 300px; height: 326px;
    background: linear-gradient(to bottom, var(--mist) 0%, #eef2e6 40%, var(--grass-light) 72%, var(--grass-dark) 100%);
    -webkit-mask-image: linear-gradient(to right, #000 55%, transparent 100%);
    mask-image: linear-gradient(to right, #000 55%, transparent 100%);
  }
  .back__headline {
    position: absolute; left: 20px; top: 12px;
    font-family: var(--script); color: var(--red);
    font-size: 22px; line-height: 26px; font-weight: 700;
    white-space: nowrap;
  }
  .back__headline span { display: block; }
  .back__headline span + span { padding-left: 30px; }
  .back__rule {
    position: absolute; left: 198px; top: 38px; width: 322px; height: 1px;
    background: var(--red);
  }
  .back__body {
    position: absolute; left: 243px; top: 49px; width: 280px;
    font-family: var(--sans); color: var(--text);
    font-size: 9.6px; line-height: 13.1px;
  }
  .back__body p + p, .back__body ul + p { margin-top: 8px; }
  .back__body p + ul { margin-top: 0; }
  .back__body p + p.back__lead { margin-top: 8px; }
  .back__list { list-style: none; }
  .back__list li { position: relative; padding-left: 12px; }
  .back__list li::before { content: "-"; position: absolute; left: 0; }
  .back__brand { left: 350px; top: 299px; }
  .back__brand .brand__mark { width: 53px; height: 53px; }
  .back__contact {
    position: absolute; left: 0; bottom: 0; width: 540px; height: 21px;
  }
  .back__contact svg { position: absolute; left: 0; top: 0; }
  .back__contact-text {
    position: absolute; right: 20px; bottom: 6px;
    font-family: var(--sans); color: #fff;
    font-size: 7.6px; white-space: nowrap;
  }
  .back__contact-text strong { font-weight: 600; }
</style>
</head>
<body>
<main class="canvas">

  <section class="flyer flyer--front" aria-label="Flyer front">
    <div class="front__photo" role="img" aria-label="Photo of a woman holding a low kung fu stance on a wooden deck against a pale grey wall"></div>
    <h1 class="front__headline"><span>Challenge</span><span>Yourself...</span></h1>
    <p class="front__body">Teaching is the highest form of<br>learning. Be a part of a professional,<br>dedicated team, delivering the<br>highest level Kung Fu...</p>
    <div class="brand front__brand">
      <div class="brand__text">
        <div class="brand__name">Copper Heron<br>Martial Arts</div>
        <div class="brand__tagline">"Challenge yourself... for life!</div>
      </div>
      <div class="brand__mark" aria-hidden="true"></div>
    </div>
    <svg class="flyer__band" width="540" height="24" viewBox="0 0 540 24" aria-hidden="true">
      <polygon points="0,0 240,0 225,24 0,24" fill="var(--red)"/>
      <polygon points="240,0 540,0 540,24 225,24" fill="var(--ink)"/>
    </svg>
  </section>

  <section class="flyer flyer--back" aria-label="Flyer back">
    <div class="back__photo" role="img" aria-label="Photo of two people in white kung fu uniforms practising forms on a sunlit lawn"></div>
    <h2 class="back__headline"><span>Seeking martial</span><span>arts instructors!</span></h2>
    <div class="back__rule"></div>
    <div class="back__body">
      <p>We train in one of the world's most effective martial art systems, Choy Li Fut Kung Fu. As an instructor, you will teach both beginner and intermediate level Kung Fu skills to adults and children at Copper Heron Martial Arts, Brisbane's premier martial arts school.</p>
      <p>As an instructor, you will:</p>
      <ul class="back__list">
        <li>Teach fundamentals to children and adults of all ages and abilities</li>
        <li>Progress student's martial arts and life skills</li>
        <li>Deliver fun and engaging classes</li>
        <li>Develop and grow your martial arts skills at an advanced level and pace</li>
      </ul>
      <p>In return, you will receive your training tuition, which includes our high level instructor training program, until qualified and then a weekly one one on one with our very own Sifu, as well as one hour training sessions, twice a week , with our team.</p>
    </div>
    <div class="brand back__brand">
      <div class="brand__text">
        <div class="brand__name">Copper Heron<br>Martial Arts</div>
        <div class="brand__tagline">"Challenge yourself... for life!</div>
      </div>
      <div class="brand__mark" aria-hidden="true"></div>
    </div>
    <div class="back__contact">
      <svg width="540" height="21" viewBox="0 0 540 21" aria-hidden="true">
        <polygon points="184,0 540,0 540,21 172,21" fill="var(--red)"/>
      </svg>
      <p class="back__contact-text">Contact us on <strong>0417 863 120</strong> to discuss your interest and suitability - ask for Sifu Rory.</p>
    </div>
  </section>

</main>
</body>
</html>
```